Pages toward Inner Calm - book cover

12/18 update: Please read the entire brief. I don’t love anything that has been provided up to today. Please use the graphics and colors I’ve attached!!!! Show me your creations.

I am looking for a book cover design. It is a mental health journal. Needs to be very warm, inviting, calming. I’m very interested in new creative ideas. It will be wire-o bound and also in hard copy front and back. Use the graphic and colors I already have attached to this file. It’s called “Pages Toward Inner Calm”. Self means soul or spirit or center. The idea of integration may be a fit here in some way. If some words need to be emphasized in the design, “Self” and “QRM” would be the most important. size 6"x9". The words on the front can be smaller and more inviting then they would normally be on a fiction paperback.

Update 12/16: I am not excited about any of the submissions so far. I’m looking forward to seeing more options.

Target Market(s)

Adults 30-60. Male and female. People who like to learn. People wanting to heal. Middle and upper income.

Industry/Entity Type

Mental health. Wellness

Font styles to use
Other font styles liked:
• Whatever font is used in my logo. i don’t know the name. I also would be open to a different font if it was warm, inviting, and calm.

Colors
0094D4
00A9DD
6FCCEA
C7EBF8
E9F6FB

Requirements
Must have
• My logo colors. The words “Pages Toward Inner Calm” and “A 13-Week QRM Exploration”
Nice to have
• I’d like to see some creative ideas. More abstract than realistic.
Should not have
• No realist art or photos.

```html
<!DOCTYPE html>
<html lang="en">
<head>
<meta charset="utf-8">
<title>Pages toward Inner Calm – Book Cover</title>
<link href="https://fonts.googleapis.com/css2?family=Arimo:wght@400;700&display=swap" rel="stylesheet">
<style>
  :root {
    --stage: #000000;
    --paper: #ecece7;
    --paper-light: #f5f5f1;
    --ink: #2b5466;
    --teal-deep: #1f4f66;
    --teal-mid: #3f8596;
    --teal-soft: #9fc3c8;
    --ember: #d4552a;
  }
  * { margin: 0; padding: 0; box-sizing: border-box; }
  html, body {
    width: 1200px;
    height: 1200px;
    overflow: hidden;
    background: var(--stage);
  }
  .canvas {
    position: relative;
    width: 1200px;
    height: 1200px;
  }
  .cover {
    position: absolute;
    left: 253px;
    top: 75px;
    width: 720px;
    height: 1078px;
    background: linear-gradient(160deg, var(--paper-light) 0%, var(--paper) 45%, #e6e6e0 100%);
    font-family: "Arimo", Arial, sans-serif;
    color: var(--ink);
    text-align: center;
  }
  .cover-title {
    position: absolute;
    top: 98px;
    left: 0;
    width: 100%;
    font-weight: 400;
    line-height: 1;
  }
  .cover-title .line-small {
    display: block;
    font-size: 46px;
    letter-spacing: 3px;
    margin-bottom: 18px;
  }
  .cover-title .line-large {
    display: block;
    font-size: 124px;
    letter-spacing: 2px;
    margin-top: 4px;
  }
  .cover-subtitle {
    position: absolute;
    top: 400px;
    left: 0;
    width: 100%;
    font-size: 26px;
    letter-spacing: 2px;
    font-weight: 400;
  }
  .cover-subtitle strong { font-weight: 700; }
  .cover-art {
    position: absolute;
    left: 0;
    top: 460px;
    width: 720px;
    height: 490px;
  }
  .cover-author {
    position: absolute;
    top: 992px;
    left: 0;
    width: 100%;
    font-size: 30px;
    letter-spacing: 6px;
    font-weight: 400;
  }
</style>
</head>
<body>
  <main class="canvas">
    <section class="cover">
      <h1 class="cover-title">
        <span class="line-small">PAGES TOWARD</span>
        <span class="line-small">INNER</span>
        <span class="line-large">CALM</span>
      </h1>
      <p class="cover-subtitle">A 13-WEEK <strong>QRM</strong> EXPLORATION</p>

      <svg class="cover-art" viewBox="0 0 720 490" role="img"
           aria-label="Watercolour illustration: a figure in teal ink with a tree growing from the head, orange coral branches, and a small seated meditator on an island reflected in still water">
        <defs>
          <radialGradient id="art-wash" cx="0.5" cy="0.55" r="0.55">
            <stop offset="0%" stop-color="var(--teal-deep)"/>
            <stop offset="45%" stop-color="var(--teal-mid)" stop-opacity="0.85"/>
            <stop offset="80%" stop-color="var(--teal-soft)" stop-opacity="0.45"/>
            <stop offset="100%" stop-color="var(--paper)" stop-opacity="0"/>
          </radialGradient>
        </defs>
        <rect x="0" y="0" width="720" height="490" fill="url(#art-wash)"/>
      </svg>

      <p class="cover-author">MARA LINDQVIST</p>
    </section>
  </main>
</body>
</html>
```